Restyle Company web site and logo

we need a wordpress design beacause after few year we need to refresh our company web site(www.velantoworks.net) & logo. We are a small company called KR Advisory focused on business intellegence, data quality, data integration, etc and based on Legnago (small town near to Verona (italy)).
During the 2014 we add to our skill develop project for MDM and Procurement.
We are Young (avg 30 years old). We want to change our logo and color templete to communicate to all cumstomer professional skill, precision and passion.

--- UPDATE --
The new site can be complitile different from the actual website.
The new Logo is now available.

Target Market(s)

B2B, mid size market, professional account

Industry/Entity Type

It Company

Font styles to use
Sans Serif

Colors
acd037
3277b5

Requirements
Must have
• Simple and clean/clear image colur. Professional site. it need to rapresent trust site.
• Must be responsive desk/mobile.
Nice to have
• different color area for different kind off business line.
• slider image.
Should not have
• classical image

```html
<!DOCTYPE html>
<html lang="en">
<head>
<meta charset="utf-8">
<title>KR Advisory</title>
<link rel="stylesheet" href="https://fonts.googleapis.com/css2?family=Arimo:wght@400;700&family=Open+Sans:wdth,wght@75,300&display=swap">
<style>
:root{
  --green:#9fc52b;
  --green-dark:#86ad1a;
  --blue:#0a6aa6;
  --brand:#1f6a9c;
  --ink:#222;
  --muted:#666;
  --grey-band:#dcdcdc;
  --footer:#9d9d9d;
  --date:#b3b3b3;
  --line:#d6d6d6;
}
*{margin:0;padding:0;box-sizing:border-box}
html,body{width:992px;height:1200px;overflow:hidden}
body{position:relative;background:#f1f1f1;font-family:"Arimo",Arial,sans-serif;color:var(--ink)}
.abs{position:absolute}
.cond{font-family:"Open Sans","Arial Narrow",sans-serif;font-stretch:75%;font-weight:300}

/* header */
.site-header{left:0;top:0;width:992px;height:124px;background:linear-gradient(#f4f4f4,#fff 40%);border-bottom:8px solid #d8d8d8}
.brand{left:96px;top:48px;display:flex;align-items:center;gap:8px;font-size:22px;color:var(--brand);font-weight:400;letter-spacing:.5px}
.brand-dot{width:22px;height:22px;border-radius:50%;background:var(--green)}
.connect{left:763px;top:17px;font-size:13.5px;color:#333;display:flex;align-items:center;gap:8px}
.social{width:18px;height:18px;border-radius:3px;background:var(--blue)}
.call{left:799px;top:44px;font-size:13.5px;color:#333}
.call span{color:var(--blue)}
.main-nav{left:306px;top:73px;width:604px;height:35px;display:flex;background:linear-gradient(#b4dc3c,var(--green-dark));border-radius:2px}
.main-nav a{display:flex;align-items:center;justify-content:center;color:#222;text-decoration:none;font-size:15px;border-right:1px solid #7e9f17;box-shadow:inset -1px 0 0 #c4e65a}
.main-nav a:last-child{border:0;box-shadow:none}

/* hero */
.hero{left:0;top:124px;width:992px;height:312px;background:var(--blue)}
.hero-photo{left:440px;top:0;width:400px;height:312px;background:linear-gradient(90deg,var(--blue) 0%,#1d3f5c 40%,#7fb7e6 62%,#3d7fb8 80%,#0b3354 100%)}
.hero-title{left:96px;top:70px;font-size:40px;color:#fff;letter-spacing:.5px;font-weight:400}
.hero-tagline{left:94px;top:118px;font-size:39px;line-height:46px;color:#fff}

/* services */
.services{left:0;top:440px;width:992px;height:138px;background:var(--grey-band);border-top:2px solid #eee}
.service{top:24px;width:260px}
.service svg{position:absolute;left:0;top:4px}
.service h3{position:absolute;left:57px;top:0;font-weight:400;font-size:18.5px;line-height:22px;color:#222;white-space:nowrap}
.service p{position:absolute;left:57px;top:24px;width:190px;font-size:10px;line-height:12px;color:#444}

/* content card */
.content{left:74px;top:605px;width:835px;height:529px;background:#fff;border:1px solid #ddd}
.section-title{font-size:37px;color:#222;line-height:1;font-weight:300}
.welcome{left:24px;top:20px}
.lead{left:24px;top:73px;width:500px;font-size:15.5px;line-height:19px;color:#111}
.intro{left:24px;top:122px;width:490px;font-size:11.3px;line-height:18.5px;color:var(--muted)}
.team-title{left:24px;top:243px}
.carousel{left:26px;top:292px;width:492px;height:180px;border:1px solid var(--line)}
.arrow{top:62px;width:15px;height:15px;border-radius:50%;background:#ccc}
.arrow svg{display:block}
.member{top:20px;width:125px;text-align:center}
.member-photo{width:125px;height:86px;border:1px solid #ddd;background:linear-gradient(135deg,#e6eef4,#9fb6c8 55%,#1e2c44)}
.member p{font-size:10.5px;line-height:14px;color:#222;margin-top:16px}
.member a{display:block;font-size:10px;color:var(--blue);text-decoration:none;margin-top:6px}

.news-title{left:571px;top:26px}
.news-item{left:576px;width:240px;height:70px}
.date{position:absolute;left:0;top:0;width:55px;height:70px;background:var(--date);color:#fff;text-align:center}
.date b{display:block;font-size:31px;line-height:36px;padding-top:3px;font-weight:300}
.date i{display:block;font-style:normal;font-size:18px;line-height:20px}
.date:after{content:"";position:absolute;right:-8px;top:12px;border:6px solid transparent;border-left:8px solid var(--date);border-right:0}
.news-item h4{position:absolute;left:69px;top:0;width:165px;font-weight:400;font-size:13.6px;line-height:16px}
.news-item p{position:absolute;left:69px;top:34px;width:165px;font-size:10.5px;line-height:14px;color:#555}
.questions{left:576px;top:381px;width:237px;height:110px;border:1px solid #ddd;background:#fff}
.questions h4{position:absolute;left:12px;top:12px;font-weight:400;font-size:18px;line-height:21px}
.q-photo{right:0;top:0;width:80px;height:79px;background:linear-gradient(90deg,#fff,#e6d3c7 45%,#b88f78)}
.q-call{left:-1px;bottom:-1px;width:237px;height:31px;background:var(--green);color:#fff;font-size:19px;line-height:31px;padding-left:21px}

/* footer */
.site-footer{left:0;top:1134px;width:992px;height:66px;background:var(--footer);border-top:3px solid #888}
.site-footer p{position:absolute;left:96px;font-size:10px;color:#222}
.footer-brand{left:830px;top:24px;font-size:11px;color:#666}
</style>
</head>
<body>

<header class="site-header abs">
  <div class="brand abs"><span class="brand-dot"></span>KR Advisory</div>
  <div class="connect abs">Connect with us: <span class="social"></span><span class="social"></span></div>
  <div class="call abs">Call: <span>02555019840</span></div>
  <nav class="main-nav abs">
    <a style="width:88px">Home</a>
    <a style="width:152px">Business Partner</a>
    <a style="width:120px">References</a>
    <a style="width:136px">Work with us</a>
    <a style="width:108px">Contacts</a>
  </nav>
</header>

<section class="hero abs">
  <div class="hero-photo abs" role="img" aria-label="Blue-toned photograph of two people shaking hands"></div>
  <h1 class="hero-title abs">KR ADVISORY</h1>
  <p class="hero-tagline abs cond">Get the Desired Information at the<br>Right Time and in the Correct Form.</p>
</section>

<section class="services abs">
  <div class="service abs" style="left:74px">
    <svg width="40" height="36" viewBox="0 0 40 36"><rect x="1" y="1" width="38" height="26" rx="2" fill="var(--blue)"/><rect x="5" y="5" width="30" height="18" fill="#fff" opacity=".15"/><rect x="16" y="27" width="8" height="5" fill="var(--blue)"/><rect x="10" y="32" width="20" height="3" fill="var(--blue)"/></svg>
    <h3>Evolution support</h3>
    <p>Do not let the problems curb your business. Evolution support was established with the aim to help our clients in all stages of the project...</p>
  </div>
  <div class="service abs" style="left:363px">
    <svg width="38" height="36" viewBox="0 0 38 36"><path d="M3 28a16 16 0 1 1 32 0z" fill="var(--blue)"/><circle cx="10" cy="22" r="2" fill="#fff"/><circle cx="13" cy="14" r="2" fill="#fff"/><circle cx="25" cy="14" r="2" fill="#fff"/><circle cx="28" cy="22" r="2" fill="#fff"/><path d="M19 26l4-12" stroke="#fff" stroke-width="2.5"/><circle cx="19" cy="26" r="3" fill="#fff"/></svg>
    <h3>Corporate Performance<br>Management</h3>
    <p style="top:46px">The information that drives your business. How many people in your company have the right information at the right time</p>
  </div>
  <div class="service abs" style="left:663px">
    <svg width="38" height="38" viewBox="0 0 38 38"><circle cx="19" cy="19" r="17" fill="var(--blue)"/><path d="M19 19V2M19 19l14.7 8.5M19 19L4.3 27.5" stroke="#fff" stroke-width="2.5"/></svg>
    <h3>Business Intelligence</h3>
    <p>Do not let the problems curb your business. Evolution support was established with the aim to help our clients in all stages of the project...</p>
  </div>
</section>

<main class="content abs">
  <h2 class="section-title cond welcome abs">WELCOME!</h2>
  <p class="lead abs">How many people in your company have the desired information at the right time and in the correct form?</p>
  <p class="intro abs">For a company it is essential to exploit the wealth of information available to make them accessible to their managers in order to help them in choosing the right business strategies (see the trend of performance, generate estimates, assume future scenarios and future strategies of response.) KR Advisory helps you to manage this process as simple and fast!</p>

  <h2 class="section-title cond team-title abs">OUR TEEM</h2>
  <div class="carousel abs">
    <span class="arrow abs" style="left:5px"><svg width="15" height="15"><path d="M9 4L5 7.5 9 11" fill="#fff"/></svg></span>
    <span class="arrow abs" style="right:5px"><svg width="15" height="15"><path d="M6 4l4 3.5L6 11" fill="#fff"/></svg></span>
    <div class="member abs" style="left:29px"><div class="member-photo" role="img" aria-label="Portrait of a team member in a suit on the phone"></div><p>Sed faucibus vitae augue<br>at faucibus.</p><a>Learn more &gt;&gt;</a></div>
    <div class="member abs" style="left:182px"><div class="member-photo" role="img" aria-label="Portrait of a team member in a suit on the phone"></div><p>Sed faucibus vitae augue<br>at faucibus.</p><a>Learn more &gt;&gt;</a></div>
    <div class="member abs" style="left:335px"><div class="member-photo" role="img" aria-label="Portrait of a team member in a suit on the phone"></div><p>Sed faucibus vitae augue<br>at faucibus.</p><a>Learn more &gt;&gt;</a></div>
  </div>

  <h2 class="section-title cond news-title abs">RECENT NEWS</h2>
  <article class="news-item abs" style="top:79px">
    <div class="date cond"><b>06</b><i>OCT</i></div>
    <h4>LUMA vince il Nordvale Cloud Inno…</h4>
    <p>Lorem ipsum dolor sit amet, consectetur adipiscing elit.</p>
  </article>
  <article class="news-item abs" style="top:173px">
    <div class="date cond"><b>06</b><i>OCT</i></div>
    <h4 style="left:73px">LUMA Spring Tour 2012</h4>
    <p style="left:73px;top:24px">Lorem ipsum dolor sit amet, consectetur adipiscing elit.</p>
  </article>
  <article class="news-item abs" style="top:267px">
    <div class="date cond"><b>06</b><i>OCT</i></div>
    <h4 style="left:73px">Nunc non bibendum nisl.</h4>
    <p style="left:73px;top:24px">Lorem ipsum dolor sit amet, consectetur adipiscing elit. Nullam condimentum libero quis est</p>
  </article>

  <aside class="questions abs">
    <div class="q-photo abs" role="img" aria-label="Photograph of a support agent wearing a headset"></div>
    <h4>Have any<br>Questions?</h4>
    <div class="q-call abs">Call us: 02555019840</div>
  </aside>
</main>

<footer class="site-footer abs">
  <p style="top:16px">KR Advisory S.r.l. - Via Corsini, 24/B - 40199 Castelbruno (CB)</p>
  <p style="top:34px">© Copyright KR Advisory 2014 All Rights Reserved.</p>
  <span class="footer-brand abs">KR Advisory</span>
</footer>

</body>
</html>
```